Veltrane Business Card - Construction Management

Create a business card for a construction management firm that owns/responsible for three other companies and include the following:
Main Company & Logo - Veltrane Management Group Ltd.
Subsidiary Company Logo only to appear on card in miniature form :
Quelbrin Industrial Services Ltd.
Halvoran Sisters Construction Inc.
Tessaly Groundworks

Contact Information for Business Card

Veltrane Management Group Ltd.
872 Brelford Road - Coville Industrial Park
RM of Danbrook
Regina, Saskatchewan
S7T 2B9
P: 306.555.0182
C: 306.555.0147
e:jtorvelli@veltrane-example.ca

Colors

Designer to choose colors to be used in the design.

Requirements
Must have
• Main Logo and small/miniature version of three subsidiary company logos.
• We would appreciate seeing a version of main logo(Veltrane Group) on front of card and other three miniature/small logos on the front of the card or version of main logo on front and other three logos on the back of the card.

```html
<!DOCTYPE html>
<html lang="en">
<head>
<meta charset="utf-8">
<title>Veltrane Business Card</title>
<link rel="stylesheet" href="https://fonts.googleapis.com/css2?family=Lato:wght@400;700;900&display=swap">
<style>
  :root {
    --page: #2a2b30;
    --card: #0f0f1a;
    --blue: #2b7fd4;
    --grey: #8c8f96;
    --light: #c9ccd2;
    --white: #ffffff;
    --maroon: #5a2226;
    --red: #d4202f;
  }
  * { box-sizing: border-box; margin: 0; padding: 0; }
  html, body { width: 1200px; height: 800px; overflow: hidden; }
  body {
    background: var(--page);
    font-family: "Lato", Arial, sans-serif;
    position: relative;
  }
  .card {
    position: absolute;
    left: 320px;
    width: 560px;
    height: 320px;
    background: var(--card);
    border-radius: 4px;
    box-shadow: 0 10px 30px rgba(0,0,0,.45);
    overflow: hidden;
  }
  .card--back { top: 50px; }
  .card--front { top: 430px; }

  /* Back: subsidiary names */
  .subsidiaries {
    position: absolute;
    inset: 0;
    display: flex;
    align-items: center;
    justify-content: space-between;
    padding: 0 38px;
  }
  .subsidiary {
    font-weight: 900;
    text-transform: uppercase;
    line-height: 1.05;
    font-size: 17px;
    display: flex;
    align-items: center;
    gap: 8px;
  }
  .subsidiary--tessaly { color: var(--white); }
  .subsidiary--quelbrin { color: var(--white); }
  .subsidiary--halvoran { color: var(--red); }
  .subsidiary__dot {
    width: 22px; height: 22px; border-radius: 50%;
    background: var(--maroon);
    flex: none;
  }

  /* Front */
  .brand {
    position: absolute;
    left: 40px; top: 48px;
    display: flex; align-items: center; gap: 14px;
  }
  .brand__mark { width: 46px; height: 46px; background: var(--blue); }
  .brand__name {
    font-weight: 900; font-size: 32px; color: var(--blue);
    letter-spacing: .5px; text-transform: uppercase;
  }
  .rule { position: absolute; }
  .rule--brand { left: 100px; top: 108px; }
  .rule--name { left: 176px; top: 184px; }

  .person {
    position: absolute; left: 40px; top: 172px;
    font-weight: 900; font-size: 19px; color: var(--blue);
    text-transform: uppercase;
  }
  .contacts {
    position: absolute; left: 40px; top: 222px;
    list-style: none;
    font-size: 13.5px; color: var(--light);
  }
  .contacts li { display: flex; align-items: center; gap: 9px; margin-bottom: 7px; }
  .contacts svg { width: 18px; height: 18px; flex: none; }

  .address {
    position: absolute; right: 36px; top: 212px;
    text-align: right; font-style: normal;
    font-size: 12.5px; line-height: 1.55; color: var(--grey);
  }
  .address__company { color: var(--blue); font-weight: 700; font-size: 13.5px; }
</style>
</head>
<body>

<section class="card card--back" aria-label="Card back with subsidiary companies">
  <div class="subsidiaries">
    <div class="subsidiary subsidiary--tessaly">Tessaly<br>Groundworks</div>
    <div class="subsidiary subsidiary--quelbrin"><span class="subsidiary__dot"></span>Quelbrin<br>Industrial</div>
    <div class="subsidiary subsidiary--halvoran">Halvoran<br>Sisters</div>
  </div>
</section>

<section class="card card--front" aria-label="Card front for Veltrane Group">
  <div class="brand">
    <span class="brand__mark"></span>
    <span class="brand__name">Veltrane Group</span>
  </div>
  <svg class="rule rule--brand" width="420" height="14" viewBox="0 0 420 14">
    <g stroke="#8c8f96" stroke-width="1.5">
      <line x1="0" y1="2" x2="420" y2="2"/>
      <line x1="0" y1="7" x2="420" y2="7"/>
      <line x1="0" y1="12" x2="420" y2="12"/>
    </g>
  </svg>

  <div class="person">Dana Reyes</div>
  <svg class="rule rule--name" width="340" height="14" viewBox="0 0 340 14">
    <g stroke="#8c8f96" stroke-width="1.5">
      <line x1="0" y1="2" x2="340" y2="2"/>
      <line x1="0" y1="7" x2="340" y2="7"/>
      <line x1="0" y1="12" x2="340" y2="12"/>
    </g>
  </svg>

  <ul class="contacts">
    <li>
      <svg viewBox="0 0 18 18"><circle cx="9" cy="9" r="8" fill="none" stroke="#2b7fd4" stroke-width="1.5"/><path d="M6 5.5l1.6-.5 1 2-1 .8a5 5 0 0 0 2.6 2.6l.8-1 2 1-.5 1.6c-3.5.3-6.8-3-6.5-6.5z" fill="#2b7fd4"/></svg>
      306.555.0182
    </li>
    <li>
      <svg viewBox="0 0 18 18"><circle cx="9" cy="9" r="8" fill="none" stroke="#2b7fd4" stroke-width="1.5"/><rect x="6.5" y="4.5" width="5" height="9" rx="1" fill="none" stroke="#2b7fd4" stroke-width="1.3"/></svg>
      306.555.0147
    </li>
    <li>
      <svg viewBox="0 0 18 18"><circle cx="9" cy="9" r="8" fill="none" stroke="#2b7fd4" stroke-width="1.5"/><rect x="5" y="6" width="8" height="6" fill="none" stroke="#2b7fd4" stroke-width="1.3"/><path d="M5 6l4 3.2L13 6" fill="none" stroke="#2b7fd4" stroke-width="1.2"/></svg>
      jtorvelli@veltrane-example.ca
    </li>
  </ul>

  <address class="address">
    <div class="address__company">Veltrane Management Group Ltd.</div>
    872 Brelford Road - Coville Industrial Park<br>
    RM of Danbrook<br>
    Regina, Saskatchewan, S7T 2B9
  </address>
</section>

</body>
</html>
```